LLC needs a business card design that emphasizes consulting and expert witness in upstream oil and g

I need a business card design for my company called Velmo Consultative Service, LLC. My expertise is in oil and gas upstream operations management to optimize performance and also as an expert witness for law firms in oil and gas upstream operations litigation.
The final design should communicate knowledge and hands-on experience as well as trust. (Velmo means rope or lasso. Perhaps "Velmo" should be in the form of a rope.) I do not like the color green in any shade. My first preference would be some shade of blue.

```html
<!DOCTYPE html>
<html lang="en">
<head>
<meta charset="utf-8">
<title>Velmo Consultative Service, LLC — Business Card</title>
<link rel="stylesheet" href="https://fonts.googleapis.com/css2?family=Oswald:wght@400;500;600&family=Open+Sans:wght@400;600&display=swap">
<style>
  :root {
    --stage: #414141;
    --card-white: #ffffff;
    --brand-blue: #1b73b9;
    --band-top: #2f8ed6;
    --band-mid: #0f63a8;
    --band-bottom: #0a4f8c;
    --back-light: #1d8fd8;
    --back-dark: #0b5fa4;
    --navy: #16324f;
    --footer-dark: #2e2e2e;
    --ink: #2b2b2b;
    --muted: #777777;
    --panel-tint: #cfe3f1;
  }
  * { box-sizing: border-box; margin: 0; padding: 0; }
  html, body {
    width: 1190px; height: 1200px; overflow: hidden;
    background: var(--stage);
  }
  .stage { position: relative; width: 1190px; height: 1200px; }

  .card {
    position: absolute; left: 269px; width: 665px; height: 399px;
    overflow: hidden;
    box-shadow: 0 4px 10px rgba(0,0,0,.55);
  }
  .card--front { top: 212px; background: var(--card-white); }
  .card--back  { top: 623px; background: var(--footer-dark); }

  /* front */
  .name-panel {
    position: absolute; left: 46px; top: 71px; width: 262px; height: 160px;
    border-radius: 26px; background: var(--panel-tint); opacity: .8;
    z-index: 0;
  }
  .person { position: absolute; left: 50px; top: 118px; z-index: 1; }
  .person__name {
    font: 500 31px/1 "Oswald", sans-serif; color: var(--brand-blue);
    letter-spacing: .5px;
  }
  .person__role {
    margin-top: 8px; font: 400 14px/1 "Open Sans", sans-serif;
    color: var(--muted); letter-spacing: 2px;
  }

  .brand { position: absolute; display: flex; flex-direction: column; align-items: center; }
  .brand--front { left: 385px; top: 60px; width: 210px; }
  .brand__mark { background: var(--navy); }
  .brand--front .brand__mark { width: 42px; height: 42px; }
  .brand__name { font-family: "Oswald", sans-serif; font-weight: 600; line-height: 1; }
  .brand--front .brand__name { font-size: 44px; color: var(--brand-blue); margin-top: 4px; }
  .brand__tagline {
    font: 600 18px/1 "Oswald", sans-serif; color: var(--navy);
    letter-spacing: .5px; white-space: nowrap;
  }
  .brand--front .brand__tagline { margin-top: 4px; }

  .phone-band {
    position: absolute; left: 0; top: 210px; width: 100%; height: 38px;
    z-index: 2;
    background: linear-gradient(to bottom, var(--band-top) 0%, var(--band-mid) 45%, var(--band-bottom) 100%);
    border-top: 2px solid #7fc0ee;
    display: flex; align-items: center; gap: 30px; padding-left: 46px;
    font: 400 22px/1 "Oswald", sans-serif; color: #fff; letter-spacing: .3px;
  }
  .phone-band b { font-weight: 600; margin-right: 4px; }

  .contact {
    position: absolute; display: flex; align-items: center; gap: 14px;
    font: 400 20px/1 "Open Sans", sans-serif; color: var(--ink);
  }
  .contact svg { width: 24px; height: 24px; flex: none; }
  .contact .social-square { width: 22px; height: 22px; background: var(--brand-blue); flex: none; }
  .contact--email { left: 46px; top: 261px; }
  .contact--web   { left: 46px; top: 297px; }
  .contact--fb    { left: 403px; top: 261px; }
  .contact--chat  { left: 403px; top: 297px; }
  .contact--address { left: 46px; top: 330px; width: 560px; }
  .address-parts { display: flex; justify-content: space-between; flex: 1; }

  /* back */
  .back-field {
    position: absolute; left: 0; top: 0; width: 100%; height: 320px;
    background: linear-gradient(to bottom, var(--back-light) 0%, #1781ca 55%, var(--back-dark) 100%);
  }
  .brand--back { left: 0; top: 78px; width: 100%; }
  .brand--back .brand__mark { width: 74px; height: 74px; }
  .brand--back .brand__name { font-size: 104px; color: #fff; margin-top: 6px; }
  .brand--back .brand__tagline { font-size: 23px; margin-top: 8px; }
  .back-footer {
    position: absolute; left: 0; top: 320px; width: 100%; height: 79px;
    display: flex; align-items: center; justify-content: center;
    font: 400 24px/1 "Open Sans", sans-serif; color: #fff;
  }
</style>
</head>
<body>
<main class="stage">

  <section class="card card--front" aria-label="Business card front">
    <div class="name-panel"></div>
    <div class="person">
      <p class="person__name">YOUR NAME</p>
      <p class="person__role">director</p>
    </div>

    <div class="brand brand--front">
      <span class="brand__mark"></span>
      <span class="brand__name">Velmo</span>
      <span class="brand__tagline">CONSULTATIVE SERVICE, LLC</span>
    </div>

    <div class="phone-band">
      <span><b>(O)</b>111.222.3333</span>
      <span><b>(M)</b>111.222.3333</span>
      <span><b>(F)</b>111.222.3333</span>
    </div>

    <p class="contact contact--email">
      <svg viewBox="0 0 24 24" aria-hidden="true"><rect x="1" y="4" width="22" height="16" rx="2" fill="#1b73b9"/><path d="M2 6l10 7 10-7" fill="none" stroke="#fff" stroke-width="2"/></svg>
      yourname@velmo.com
    </p>
    <p class="contact contact--web">
      <svg viewBox="0 0 24 24" aria-hidden="true"><rect x="1" y="1" width="22" height="22" rx="3" fill="#1b73b9"/><circle cx="12" cy="12" r="7" fill="none" stroke="#fff" stroke-width="1.6"/><ellipse cx="12" cy="12" rx="3" ry="7" fill="none" stroke="#fff" stroke-width="1.4"/><path d="M5 12h14" stroke="#fff" stroke-width="1.4"/></svg>
      www.velmo.com
    </p>
    <p class="contact contact--fb"><span class="social-square"></span>velmo</p>
    <p class="contact contact--chat"><span class="social-square"></span>velmo</p>
    <div class="contact contact--address">
      <svg viewBox="0 0 24 24" aria-hidden="true"><rect x="1" y="1" width="22" height="22" rx="3" fill="#1b73b9"/><path d="M12 5a5 5 0 0 0-5 5c0 4 5 9 5 9s5-5 5-9a5 5 0 0 0-5-5z" fill="#fff"/><circle cx="12" cy="10" r="2" fill="#1b73b9"/></svg>
      <span class="address-parts">
        <span>your address</span><span>•</span><span>Orlen</span><span>•</span><span>Caldera</span><span>•</span><span>40218</span><span>•</span><span>USA</span>
      </span>
    </div>
  </section>

  <section class="card card--back" aria-label="Business card back">
    <div class="back-field"></div>
    <div class="brand brand--back">
      <span class="brand__mark"></span>
      <span class="brand__name">Velmo</span>
      <span class="brand__tagline">CONSULTATIVE SERVICE, LLC</span>
    </div>
    <p class="back-footer">www.velmo.com</p>
  </section>

</main>
</body>
</html>
```